Award-winnning Estate Agent needs a premium version of their 'For Sale' board design

We need a premium option for our 'For Sale' board design. We have a standard board that is attached to this brief, but were are looking to have a premium design version that we will use when selling exclusive properties. Our company name is Harbour Lane Estates and the name for this is exclusive selection is: 'The Harbour Collection'. The design needs to work with our current brand, but have a distinctive PREMIUM feel to it. I have uploaded the barnd guidelines and also some of the exisisting logo variations. We do NOT need a new logo but feel free to play around with colours, fonts, sizes etc. for the sign.

Target Market(s)

Property buyers & house hunters

Industry/Entity Type

Real Estate - Residential Property

Font styles to use
Sans Serif

Requirements
Must have
• A premium fee, must be square design, must be easy to read when driving past the sign
Nice to have
• I'm open ot ideas

```html
<!DOCTYPE html>
<html lang="en">
<head>
<meta charset="utf-8">
<title>Harbour Lane Estates – For Sale Board</title>
<link rel="stylesheet" href="https://fonts.googleapis.com/css2?family=Anton&family=Oswald:wght@300&family=Inter:wght@600&family=Roboto:wght@700&display=swap">
<style>
  :root {
    --page-bg: #e3e3e3;
    --board-white: #ffffff;
    --navy: #2e2d82;
    --plum: #452d72;
    --sky: #5ba3d0;
    --steel: #4569a6;
    --brand-name: #3f2a72;
  }
  * { margin: 0; padding: 0; box-sizing: border-box; }
  html, body {
    width: 1200px;
    height: 1200px;
    overflow: hidden;
    background: var(--page-bg);
  }
  .sale-board {
    position: absolute;
    left: 100px;
    top: 100px;
    width: 1000px;
    height: 1000px;
    background: var(--board-white);
    overflow: hidden;
  }
  .top-rule {
    position: absolute;
    left: 0; top: 0;
    width: 100%;
    height: 13px;
    background: var(--navy);
  }
  .headline {
    position: absolute;
    left: 0; top: 52px;
    width: 1000px;
    height: 210px;
  }
  .brand-lockup {
    position: absolute;
    left: 0; top: 300px;
    width: 100%;
    height: 130px;
    display: flex;
    align-items: center;
    justify-content: center;
    gap: 26px;
  }
  .brand-mark {
    width: 84px;
    height: 84px;
    background: var(--steel);
  }
  .brand-name {
    font-family: "Inter", sans-serif;
    font-weight: 600;
    font-size: 66px;
    letter-spacing: -0.5px;
    color: var(--brand-name);
    white-space: nowrap;
  }
  .contact-panel {
    position: absolute;
    left: 0; top: 480px;
    width: 100%;
    height: 420px;
    background: linear-gradient(to bottom, var(--sky) 0%, var(--sky) 22%, var(--steel) 100%);
  }
  .panel-notch {
    position: absolute;
    left: 0; top: 480px;
    width: 100%;
    height: 30px;
  }
  .collection-name {
    position: absolute;
    left: 0; top: 540px;
    width: 100%;
    text-align: center;
    font-family: "Oswald", sans-serif;
    font-weight: 300;
    font-size: 72px;
    line-height: 84px;
    letter-spacing: 10px;
    padding-left: 10px;
    color: var(--board-white);
  }
  .phone-number {
    position: absolute;
    left: 0; top: 628px;
    width: 1000px;
    height: 180px;
  }
  .web-pill-frame {
    position: absolute;
    left: 40px; top: 830px;
    width: 920px;
    height: 124px;
    border-radius: 62px;
    background: var(--board-white);
  }
  .web-pill {
    position: absolute;
    left: 52px; top: 842px;
    width: 896px;
    height: 100px;
    border-radius: 50px;
    background: var(--navy);
    color: var(--board-white);
    font-family: "Roboto", sans-serif;
    font-weight: 700;
    font-size: 50px;
    line-height: 100px;
    text-align: center;
    letter-spacing: -0.3px;
  }
</style>
</head>
<body>
  <main class="sale-board">
    <div class="top-rule"></div>

    <svg class="headline" viewBox="0 0 1000 210" aria-label="For Sale">
      <defs>
        <linearGradient id="headline-fill" x1="0" y1="0" x2="0" y2="1">
          <stop offset="0" stop-color="#5ba3d0"/>
          <stop offset="1" stop-color="#452d72"/>
        </linearGradient>
      </defs>
      <text x="52" y="202" textLength="896" lengthAdjust="spacingAndGlyphs"
            font-family="Anton, sans-serif" font-size="262" fill="url(#headline-fill)">FOR SALE</text>
    </svg>

    <div class="brand-lockup">
      <div class="brand-mark"></div>
      <div class="brand-name">Harbour Lane Estates</div>
    </div>

    <div class="contact-panel"></div>
    <svg class="panel-notch" viewBox="0 0 1000 30" aria-hidden="true">
      <polygon points="470,0 530,0 500,30" fill="#ffffff"/>
    </svg>

    <div class="collection-name">HARBOUR COLLECTION</div>

    <svg class="phone-number" viewBox="0 0 1000 180" aria-label="01632 960418">
      <text x="48" y="168" textLength="904" lengthAdjust="spacingAndGlyphs"
            font-family="Anton, sans-serif" font-size="200" fill="#ffffff">01632 960418</text>
    </svg>

    <div class="web-pill-frame"></div>
    <div class="web-pill">www.harbourlaneestates.co.uk</div>
  </main>
</body>
</html>
```